Consulting business card

*1) An Overview:* The business is simply a financial transaction wherein I
offer to provide advice to financial holders of commercial real estate
mortgages (which are sub-performing or non-performing), and said holders
are desirous of selling said mortgages which I will offer advice to said
holders in the purchase of said mortgages. Please note the attached copy
of a proposed line-by-line business card which starts with the 1st line
"KRW Advisory, LLC" with the 2nd line "Purchase of Commercial Mortgage
Loan" and the 3rd line "Sub-performing and Non-performing" is my desired
copy subject to any suggested changes. Please ignore the the copy below
the aforementioned proposed card/copy as it will be activated at a later
date.and advise
*2) The Target Market:* I contact and advise senior officers in banks,
insurance companies, and financial institutions such as CEOs, CFOs, COOs,
and Loan Mitigation Officers: the senior officers are tasked with the
removal of sub-performing and non-performing commercial real estate loans
from their real estate portfolios. The desired market is targeted at $1-10
million USD and located in the US.
*3) Design Specifics: *STYLE should be conservative and be representative
of the financial market contacts; COLOR might show a rich forest green
element, a gold foil accent, and subtle black printing, however,
alternatively, silver foil accent(s) with strong black print would seem in
harmony with the services offered, however, I would appreciate any artful
suggestions; IMAGERY should be subtle (no logo can be strong enough to make
an immediate impact): the quality should make the recipient feel he/she has
just met an experienced and competent financial adviser (I have over 55
years of successful financial and business experience).
720.217.6154davidfredrickjones@gmail.com

```html
<!DOCTYPE html>
<html lang="en">
<head>
<meta charset="utf-8">
<title>KRW Advisory, LLC — Business Card</title>
<link rel="stylesheet" href="https://fonts.googleapis.com/css2?family=Gelasio:wght@400;700&display=swap">
<style>
  :root {
    --page-bg: #ece9e4;
    --card-green: #1f9a58;
    --card-green-deep: #178a4c;
    --rule-red: #e0261c;
    --rule-white: #d9efe2;
    --ink: #0c140f;
  }
  html, body {
    margin: 0;
    width: 1200px;
    height: 1000px;
    overflow: hidden;
    background: var(--page-bg);
  }
  .canvas {
    width: 1200px;
    height: 1000px;
    display: flex;
    align-items: center;
    justify-content: center;
  }
  .business-card {
    position: relative;
    width: 1050px;
    height: 600px;
    background: radial-gradient(ellipse at 50% 45%, var(--card-green) 0%, var(--card-green-deep) 100%);
    box-shadow: 0 6px 18px rgba(0,0,0,0.18);
    font-family: "Gelasio", Georgia, serif;
    color: var(--ink);
  }
  .frame-red {
    position: absolute;
    inset: 16px;
    border: 2px solid var(--rule-red);
  }
  .frame-white {
    position: absolute;
    inset: 28px;
    border: 3px solid var(--rule-white);
  }
  .card-copy {
    position: absolute;
    inset: 0;
    display: flex;
    flex-direction: column;
    align-items: center;
    justify-content: center;
    text-align: center;
    padding-top: 20px;
  }
  .company-name {
    margin: 0;
    font-size: 74px;
    font-weight: 700;
    line-height: 1.05;
  }
  .service-line {
    margin: 0;
    font-size: 48px;
    font-weight: 400;
    line-height: 1.1;
  }
  .loan-status {
    margin: 0;
    font-size: 38px;
    font-weight: 400;
    line-height: 1.2;
  }
</style>
</head>
<body>
<main class="canvas">
  <section class="business-card">
    <div class="frame-red"></div>
    <div class="frame-white"></div>
    <div class="card-copy">
      <h1 class="company-name">KRW Advisory, LLC</h1>
      <p class="service-line">Purchase of Commercial Mortgage Loan</p>
      <p class="loan-status">Sub-performing and Non-performing</p>
    </div>
  </section>
</main>
</body>
</html>
```